Design for Screen Wash Tablet Tube New product

I have a tube which holds screenwash tablets which I need Label created for... Label is 90mm x 90mm. It must include
> logo attached,
>the catchphrase ( drop,dissolve,wash. )
>6 Tablets inside
>1 Tablet makes 5 litres screen wash
>Room for ingredients section( around 20 words)
> Caution - Harmful if swallowed. May cause skin Irritation or eye damage. Do not eat,drink or smoke when using this product. If medical advice is needed have product packaging to hand. Store in a clean dry place.
>Keep out of reach of Children
>Barcode area
>Directions of use
Place tablet in Screenwash bottle
Simply add water
>Product will take approximately 5-10 minutes to fully dissolve.
>3 harmful logo attached
>Cherry Fragrance
Target Market(s)
retail sector - grocery fmcg and car/auto stores
Industry/Entity Type
car care

```html
<!DOCTYPE html>
<html lang="en">
<head>
<meta charset="utf-8">
<title>ShineWell Screen Wash Tablets Label</title>
<link href="https://fonts.googleapis.com/css2?family=Poppins:wght@600;700;800&family=Montserrat:wght@700&display=swap" rel="stylesheet">
<style>
  :root {
    --label-blue: #1f4e9f;
    --band-black: #111111;
    --sun-yellow: #fde22f;
    --brand-red: #e3202b;
    --paper: #ffffff;
    --ink: #111111;
    --hazard-red: #e3202b;
  }
  * { box-sizing: border-box; margin: 0; padding: 0; }
  html, body { width: 1191px; height: 1200px; overflow: hidden; background: var(--paper); }
  .canvas {
    position: relative; width: 1191px; height: 1200px; overflow: hidden;
    border: 2px solid var(--ink);
  }
  .label {
    position: absolute; left: 0; top: 0;
    width: 1200px; height: 1191px;
    transform-origin: 0 0;
    transform: translateY(1200px) rotate(-90deg);
    background: var(--paper);
  }
  .front { position: absolute; left: 0; top: 0; width: 1200px; height: 410px; background: var(--paper); }
  .count-badge {
    position: absolute; left: 67px; top: 232px; width: 135px; height: 140px;
    background: var(--brand-red); color: var(--paper);
    display: flex; flex-direction: column; align-items: center; justify-content: center;
    font-family: "Poppins", sans-serif; font-weight: 800; line-height: 1;
  }
  .count-badge .count-number { font-size: 76px; }
  .count-badge .count-unit { font-size: 22px; margin-top: 4px; }
  .brand-name {
    position: absolute; left: 294px; top: 112px; width: 559px; height: 224px;
    display: flex; align-items: center; justify-content: center;
    font-family: "Poppins", sans-serif; font-weight: 800; font-size: 88px;
    color: var(--brand-red); letter-spacing: -1px;
  }
  .catchphrase { position: absolute; left: 866px; top: 178px; width: 260px; height: 240px; }
  .catchphrase svg { position: absolute; inset: 0; width: 100%; height: 100%; }
  .catchphrase-text {
    position: absolute; inset: 0; display: flex; flex-direction: column;
    align-items: center; justify-content: center;
    font-family: "Poppins", sans-serif; font-weight: 800; font-size: 36px; line-height: 1.45;
    color: var(--ink);
  }
  .yield-band {
    position: absolute; left: 0; top: 410px; width: 1200px; height: 60px;
    background: var(--band-black); color: var(--paper);
    font-family: "Montserrat", sans-serif; font-weight: 700; font-size: 27px;
    letter-spacing: 6.8px; display: flex; align-items: center; padding-left: 48px;
    white-space: nowrap;
  }
  .yield-band .yield-highlight { color: var(--sun-yellow); }
  .back { position: absolute; left: 0; top: 476px; width: 1200px; height: 715px; background: var(--label-blue); }
  .section-tab {
    position: absolute; left: 0; background: var(--sun-yellow); color: var(--ink);
    font-family: "Poppins", sans-serif; font-weight: 600; font-size: 22px;
    display: flex; align-items: center; white-space: nowrap;
  }
  .directions-tab { top: 55px; width: 510px; height: 54px; padding-left: 76px; }
  .caution-tab { top: 284px; width: 339px; height: 53px; padding-left: 76px; }
  .copy-line {
    position: absolute; left: 76px; color: var(--paper);
    font-family: "Poppins", sans-serif; font-weight: 600; font-size: 19px; white-space: nowrap;
    line-height: 1; transform: translateY(-50%);
  }
  .copy-line.warning { color: var(--brand-red); }
  .ingredients { position: absolute; left: 814px; top: 38px; width: 330px; color: var(--paper); font-family: "Poppins", sans-serif; }
  .ingredients-title { font-weight: 600; font-size: 23px; letter-spacing: 0.5px; line-height: 28px; white-space: nowrap; }
  .ingredients-kicker { font-weight: 700; font-size: 10px; letter-spacing: 9px; margin-top: 26px; line-height: 12px; }
  .ingredients-list { font-weight: 700; font-size: 12px; line-height: 37.5px; margin-top: 7px; white-space: nowrap; }
  .hazards { position: absolute; left: 820px; top: 396px; display: flex; gap: 6px; }
  .hazard { width: 100px; height: 100px; background: var(--paper); }
  .barcode-area {
    position: absolute; left: 881px; top: 508px; width: 207px; height: 121px;
    background: var(--paper);
  }
</style>
</head>
<body>
<div class="canvas">
  <div class="label">
    <section class="front">
      <div class="count-badge"><span class="count-number">6</span><span class="count-unit">TABLETS</span></div>
      <div class="brand-name">ShineWell</div>
      <div class="catchphrase">
        <svg viewBox="0 0 236 236" preserveAspectRatio="none" aria-hidden="true">
          <polygon fill="var(--sun-yellow)" points="233,118 210.7,142.9 217.6,175.5 185.9,185.9 175.5,217.6 142.9,210.7 118,233 93.1,210.7 60.5,217.6 50.1,185.9 18.4,175.5 25.3,142.9 3,118 25.3,93.1 18.4,60.5 50.1,50.1 60.5,18.4 93.1,25.3 118,3 142.9,25.3 175.5,18.4 185.9,50.1 217.6,60.5 210.7,93.1"/>
        </svg>
        <div class="catchphrase-text"><span>DROP</span><span>DISSOLVE</span><span>WASH</span></div>
      </div>
    </section>

    <div class="yield-band">1 TABLET MAKES&nbsp;<span class="yield-highlight">5 LITRES</span>&nbsp;SCREEN WASH</div>

    <section class="back">
      <div class="section-tab directions-tab">DIRECTIONS OF USE</div>
      <p class="copy-line" style="top:137px">Place tablet in Screenwash bottle</p>
      <p class="copy-line" style="top:190px">Simply add water</p>
      <p class="copy-line" style="top:243px">Product will take approximately 5-10 minutes to fully dissolve.</p>

      <div class="section-tab caution-tab">CAUTION</div>
      <p class="copy-line" style="top:360px">Harmful if swallowed.</p>
      <p class="copy-line" style="top:415px">May cause skin Irritation or eye damage.</p>
      <p class="copy-line" style="top:469px">Do not eat,drink or smoke when using this product.</p>
      <p class="copy-line" style="top:521px">If medical advice is needed have product packaging to hand.</p>
      <p class="copy-line" style="top:573px">Store in a clean dry place.</p>
      <p class="copy-line warning" style="top:625px">Keep out of reach of Children</p>

      <div class="ingredients">
        <h2 class="ingredients-title">INGREDIENTS SECTION</h2>
        <p class="ingredients-kicker">LOREM</p>
        <p class="ingredients-list">
          IPSUM DOLOR SIT AMET, CONSECTETUER<br>
          ADIPISCING ELIT, SED DIAM NONUMMY<br>
          NIBH EUISMOD TINCIDUNT UT LAOREET<br>
          DOLORE MAGNA ALIQUAM ERAT
        </p>
      </div>

      <div class="hazards">
        <svg class="hazard" viewBox="0 0 100 100" role="img" aria-label="Hazard pictogram: environmental hazard">
          <polygon points="50,6 94,50 50,94 6,50" fill="#fff" stroke="var(--hazard-red)" stroke-width="7"/>
          <rect x="32" y="34" width="36" height="30" fill="#8a8a8a"/>
        </svg>
        <svg class="hazard" viewBox="0 0 100 100" role="img" aria-label="Hazard pictogram: corrosive">
          <polygon points="50,6 94,50 50,94 6,50" fill="#fff" stroke="var(--hazard-red)" stroke-width="7"/>
          <rect x="32" y="34" width="36" height="30" fill="#8a8a8a"/>
        </svg>
        <svg class="hazard" viewBox="0 0 100 100" role="img" aria-label="Hazard pictogram: exclamation mark">
          <polygon points="50,6 94,50 50,94 6,50" fill="#fff" stroke="var(--hazard-red)" stroke-width="7"/>
          <path d="M44 28 H56 L53 60 H47 Z" fill="#111"/>
          <circle cx="50" cy="69" r="5.5" fill="#111"/>
        </svg>
      </div>

      <div class="barcode-area" role="img" aria-label="Barcode area"></div>
    </section>
  </div>
</div>
</body>
</html>
```